Business card for Eyelash extension salon in Beverly Hills,California USA

We need new business card for our salon in Beverly Hills. The salon name is 'Lumarra' . We would like to have...Business name: Lumarra Name of person: will provide later Address 6128 N.Corbel Ridge Blvd Beverly Hills , CA 90210 Phone: will provide later (Text only) Web: www.lumarrastudio-example.com Pictogrid icon, Friendvale icon follow us for seasonal campaign and news @lumarrastudioexample Design should look elegant, high-end, clean, simple, cohesive with my brand. Please refer my brand board. Business name color will be metallic bronzy color. Im thinking grey background or white background. Thanks

Target Market(s)

25-35. Gender neutral. People who are in Entertainment business industry.
This is High-end Eyelash extension salon in Beverly Hills

Industry/Entity Type

Beauty Salon

Contact Information for Business Card

Business name: Lumarra
Name of person: will provide later
Address 6128 N.Corbel Ridge Blvd Beverly Hills , CA 90210
Phone: will provide later (Text only)
Web: www.lumarrastudio-example.com
Pictogrid icon, Friendvale icon
follow us for seasonal campaign and news @lumarrastudioexample

Requirements
Must have
• Beautiful, elegant, clean and simple look but very attractive and modern
Should not have
• We don't like too clutter, too busy designs.

```html
<!DOCTYPE html>
<html lang="en">
<head>
<meta charset="utf-8">
<title>Lumarra Business Card</title>
<link href="https://fonts.googleapis.com/css2?family=Playfair+Display:ital,wght@0,400;0,700;1,400&display=swap" rel="stylesheet">
<style>
  :root {
    --bg: #a2a2a2;
    --paper: #ffffff;
    --bronze: #8a6446;
    --bronze-dark: #7a5a42;
    --bronze-light: #94704f;
    --ink: #5a5a5a;
    --rule: #d9c9bc;
    --serif: "Playfair Display", Georgia, serif;
  }
  * { margin: 0; padding: 0; box-sizing: border-box; }
  html, body { width: 1200px; height: 900px; overflow: hidden; background: var(--bg); }
  body { position: relative; font-family: var(--serif); }

  .card {
    position: absolute;
    left: 250px;
    width: 700px;
    height: 400px;
    border-radius: 28px;
    overflow: hidden;
    box-shadow: 0 10px 24px rgba(0,0,0,0.18);
  }

  /* Front */
  .card-front { top: 40px; background: var(--paper); }
  .front-wordmark {
    position: absolute; top: 62px; left: 0; right: 0;
    text-align: center; color: var(--bronze);
    font-size: 66px; font-weight: 400; letter-spacing: 1px;
  }
  .holder { position: absolute; left: 70px; top: 190px; width: 230px; text-align: right; }
  .holder-name { color: var(--bronze); font-weight: 700; font-size: 30px; letter-spacing: 0.5px; text-transform: uppercase; }
  .holder-role { color: var(--ink); font-size: 17px; margin-top: 4px; }
  .divider { position: absolute; left: 330px; top: 185px; width: 1px; height: 105px; background: var(--rule); }
  .contacts { position: absolute; left: 355px; top: 190px; list-style: none; }
  .contacts li { display: flex; align-items: center; gap: 12px; height: 32px; color: var(--ink); font-size: 18px; }
  .contacts svg { width: 17px; height: 17px; flex: none; }
  .contacts .web { color: var(--bronze); }
  .address-band {
    position: absolute; left: 0; right: 0; top: 322px; height: 44px;
    background: var(--bronze);
    color: #fff; font-size: 18px;
    display: flex; align-items: center; padding-left: 60px;
  }

  /* Back */
  .card-back {
    top: 470px;
    background: linear-gradient(135deg, var(--bronze-light) 0%, var(--bronze-dark) 100%);
    color: #fff;
  }
  .back-wordmark {
    position: absolute; top: 92px; left: 0; right: 0;
    text-align: center; font-size: 72px; font-weight: 400; letter-spacing: 1px;
  }
  .socials { position: absolute; top: 232px; left: 0; right: 0; display: flex; justify-content: center; gap: 28px; font-size: 15px; }
  .socials span { display: flex; align-items: center; gap: 8px; }
  .socials i { width: 12px; height: 12px; border-radius: 50%; background: #fff; display: block; }
  .follow { position: absolute; bottom: 52px; left: 0; right: 0; text-align: center; font-size: 17px; }
</style>
</head>
<body>

<section class="card card-front" aria-label="Card front">
  <div class="front-wordmark">Lumarra</div>
  <div class="holder">
    <div class="holder-name">Mira Callow</div>
    <div class="holder-role">Manager</div>
  </div>
  <div class="divider"></div>
  <ul class="contacts">
    <li>
      <svg viewBox="0 0 24 24" aria-hidden="true"><path fill="#5a5a5a" d="M6.6 10.8c1.4 2.8 3.8 5.1 6.6 6.6l2.2-2.2c.3-.3.7-.4 1-.2 1.1.4 2.300.6 3.6.6.6 0 1 .4 1 1V20c0 .6-.4 1-1 1C10.6 21 3 13.4 3 4c0-.6.4-1 1-1h3.5c.6 0 1 .4 1 1 0 1.3.2 2.5.6 3.6.1.3 0 .7-.2 1z"/></svg>
      310-555-0148
    </li>
    <li>
      <svg viewBox="0 0 24 24" aria-hidden="true"><rect x="2" y="5" width="20" height="14" rx="1.5" fill="#5a5a5a"/><path d="M3 6l9 7 9-7" fill="none" stroke="#fff" stroke-width="1.6"/></svg>
      info@lumarrastudio-example.com
    </li>
    <li class="web">
      <svg viewBox="0 0 24 24" aria-hidden="true"><circle cx="12" cy="12" r="10" fill="#5a5a5a"/><path d="M2 12h20M12 2c3 3 3 17 0 20M12 2c-3 3-3 17 0 20M4 7h16M4 17h16" fill="none" stroke="#fff" stroke-width="1.2"/></svg>
      www.lumarrastudio-example.com
    </li>
  </ul>
  <div class="address-band">6128 N.Corbel Ridge Blvd Solano Crest &nbsp;CA 90299</div>
</section>

<section class="card card-back" aria-label="Card back">
  <div class="back-wordmark">Lumarra</div>
  <div class="socials">
    <span><i></i>Friendvale</span>
    <span><i></i>Pictogrid</span>
  </div>
  <div class="follow">Follow us for seasonal campaign and news @lumarrastudioexample</div>
</section>

</body>
</html>
```